Creative UI design for web application

I need a new UI design for my web application. It will be used by small and micro business owners to plan & implement growth tactics.

I've attached the current design (which I'm open to be changed) - but in particular I need to design the centre of the screen, where the work actually happens.

There needs to be place for a title (YOUR BUSINESS) and description (say 1-2 paragraphs of text) - and am happy to include icons or imagery where makes sense. It may make sense for the user to be able to upload their business logo and name, for example.

This screen will be used by the business owner to understand the real value they offer potential customers and their point of difference - why they exist and why potential customers should care.

They'll use the information they put into this screen to plan things like their messaging.

Following that, there needs to be 2 sections in the dashboard.

The first section is titled "WHO YOU ARE"

The first section will include a number of boxes that the user can input information into, as follows:

- Logo
- Business name
- Business tag line
- Business vision
- Business bio
- Brand colours (these should end up as swatches based on the colour code they enter) - the colour code for each colour swatch should also be visible.
- Key competitors
- SWOT analysis (boxes to enter their strengths, weaknesses, opportunities and threats).

The second section is titled "WHY YOU EXIST"

The second section will include a number of boxes that the user can input information (text) into, as follows:

- Who are your ideal customers?
- What problem are you trying to solve for them?
- What pain points will this remove for them?
- How do you solve it?
- How else could this problem be solved?
- Who offers these other solutions?
- Why is your solution better?
- How much does your solution cost?
- What value are you providing to justify this cost?
- How will this make their life/job easier/better?

They should be able to write a decent amount of information in the boxes.

There should ideally be a place for a description for each of these text fields (for both section 1 & 2) as well so I can give them a little bit more direction around what to put in the box. Alternatively there could be a little icon (say a question mark or "i") that they could click on to view instructions. The instructions will be around 2-4 sentences long for each text field.

You have 2 options:

a) This all needs to appear on the one screen, and the navigation needs to be visible (as per the example attached but feel free to recreate this navigation)

Note: the page can scroll below the fold - but please provide the design for the full length of the page.

b) Potentially the 2 sections could actually be in 2 different items in the menu - YOUR BUSINESS and YOUR VALUE (which would sit next to YOUR BUSINESS and before YOUR CUSTOMER in the screenshot provided). feel free to design them as 2 separate screens if you prefer.

I have attached a screenshot of the app as it stands today (screen shot 2017) which would still exist in the new design but under a different section (the learn section from the plan2 mockup attached)

I have mocked up how this new screen could look if broken into 2 and that's also attached. If you can make this come to life - and look more engaging that would be helpful! :)

Target Market(s)

Small and micro business owners

Industry/Entity Type

Marketing

Number of Pages Required

1 page

Font styles to use
Sans Serif
Other font styles liked:
• Montserrat

Colors
87cfc6
d2a4cc
ffffff
85cae6
e8e8e8
5c5c5c

Requirements
Must have
• Use of my brand colours: #cc8eb2, #76d6c8, #68c7ff as well as white and #595959. Must be visually pleasing / engaging, designed for desktop (as it's a desktop application), really easy to use / navigate.
• Use font Montserrat light & Montserrat Regular or Bold. Mostly should be Montserrat light.
Nice to have
• Would be nice to see how this would look on mobile (as the application is responsive) but this is not mandatory.
Should not have
• Should not look too corporate or dry.

```html
<!DOCTYPE html>
<html lang="en">
<head>
<meta charset="utf-8">
<title>Budline – Your Business</title>
<link rel="stylesheet" href="https://fonts.googleapis.com/css2?family=Montserrat:wght@300;400;500;600;700&display=swap">
<style>
:root{
  --pink:#cc8eb2;
  --teal:#76d6c8;
  --blue:#68c7ff;
  --ink:#595959;
  --bar-dark:#3c3c3c;
  --tab-dark:#555555;
  --bar-grey:#7f7f7f;
  --panel:#ebebeb;
  --panel-line:#dcdcdc;
  --field-line:#d4d4d4;
  --footer:#d9d9d9;
  --white:#ffffff;
}
*{box-sizing:border-box;margin:0;padding:0}
html,body{width:1069px;height:1200px;overflow:hidden;background:var(--white)}
body{font-family:"Montserrat",sans-serif;font-weight:300;color:var(--ink);position:relative}

.topbar{height:48px;background:var(--bar-dark);position:relative}
.brand{position:absolute;left:16px;top:14px;color:var(--white);font-weight:400;font-size:19px;letter-spacing:.5px;display:flex;align-items:center;gap:7px}
.brand-dot{width:9px;height:9px;border-radius:50%;background:var(--teal)}
.main-nav{position:absolute;left:201px;top:7px;display:flex;height:41px}
.main-nav a{display:flex;align-items:center;padding:0 16px;background:var(--tab-dark);color:var(--white);font-weight:500;font-size:12.5px;letter-spacing:.6px;text-decoration:none}
.main-nav a.active{background:var(--teal)}
.user-nav{position:absolute;right:16px;top:11px;display:flex;gap:14px}
.user-nav a{display:flex;align-items:center;gap:6px;color:var(--white);font-weight:600;font-size:12px;letter-spacing:.4px;text-decoration:none}
.user-nav .ico{width:26px;height:26px;border-radius:50%;background:var(--blue);display:flex;align-items:center;justify-content:center}

.subbar{height:36px;background:var(--bar-grey);padding-left:201px;display:flex}
.subbar a{display:flex;align-items:center;padding:0 16px;color:var(--white);font-weight:500;font-size:12.5px;letter-spacing:.5px;text-decoration:none}
.subbar a.active{background:var(--pink)}

.intro{padding:20px 12px 0 14px;font-size:13px;line-height:19.7px;letter-spacing:-.2px}
.intro p+p{margin-top:19.7px}

.panels{position:absolute;top:309px;left:16px;width:1036px;display:flex;justify-content:space-between;align-items:flex-start}
.panel{width:506px;background:var(--panel);border:1px solid var(--panel-line);border-top:none;position:relative}
.panel-head{height:41px;margin:0 -1px;display:flex;align-items:center;padding-left:17px;color:var(--white);font-weight:600;font-size:18px;letter-spacing:.6px}
.panel.who .panel-head{background:var(--pink)}
.panel.why .panel-head{background:var(--teal)}
.panel-body{padding:14px 16px 16px}
.field{margin-bottom:12.5px}
.field label{display:block;font-size:13.5px;line-height:16px;margin:0 0 10px -1px}
.row{display:flex;align-items:center;gap:8px}
.input{height:33px;background:var(--white);border:1px solid var(--field-line);flex:1;font-size:13.5px;display:flex;align-items:center;padding-left:9px}
.btn{height:33px;background:var(--blue);color:var(--white);border:none;font-family:inherit;font-size:13.5px;display:flex;align-items:center;justify-content:center}
.btn.upload{width:78px;font-weight:400}
.btn.submit{width:102px;font-weight:600;letter-spacing:.6px;font-size:13px}
.info{flex:none;width:18px;height:18px;margin-left:8px;display:block}
.why .panel-body .input{flex:none;width:448px}
.swatch-btn{width:33px;height:33px;background:var(--white);border:1px solid var(--field-line);display:flex;align-items:center;justify-content:center}
.actions{display:flex;justify-content:flex-end;margin-top:4px}
.why .actions{margin-top:7px}

.picker{position:absolute;left:21px;top:479px;width:181px;height:98px;background:var(--white);border:1px solid var(--field-line);padding:9px 9px;display:grid;grid-template-columns:repeat(6,22px);grid-auto-rows:22px;column-gap:6px;row-gap:6px;box-shadow:0 1px 3px rgba(0,0,0,.08)}
.picker::before{content:"";position:absolute;left:11px;top:-7px;border:6px solid transparent;border-top:none;border-bottom:7px solid var(--field-line)}
.picker span{border:1px solid #cfcfcf;position:relative}
.picker span i{position:absolute;inset:2px}

.footer{position:absolute;left:0;right:0;bottom:0;height:41px;background:var(--footer);display:flex;align-items:center;justify-content:center;font-size:12.5px}
</style>
</head>
<body>
<header class="topbar">
  <div class="brand"><span>BUDLINE</span><span class="brand-dot"></span></div>
  <nav class="main-nav">
    <a class="active" href="#">PLAN</a><a href="#">LEARN</a><a href="#">REMEMBER</a>
  </nav>
  <nav class="user-nav">
    <a href="#"><span class="ico"><svg width="14" height="14" viewBox="0 0 14 14" fill="none" stroke="#fff" stroke-width="1.3"><circle cx="7" cy="4.5" r="2.8"/><path d="M1.8 13c.6-3 2.6-4.4 5.2-4.4s4.6 1.4 5.2 4.4"/></svg></span>MY PROFILE</a>
    <a href="#"><span class="ico"><svg width="15" height="15" viewBox="0 0 15 15" fill="none" stroke="#fff" stroke-width="1.4"><path d="M11 3.6A5.3 5.3 0 1 0 11 11.4"/><path d="M6 7.5h8M11.5 5l2.5 2.5-2.5 2.5"/></svg></span>LOG OUT</a>
  </nav>
</header>
<nav class="subbar">
  <a class="active" href="#">YOUR BUSINESS</a><a href="#">YOUR CUSTOMERS</a><a href="#">YOUR GOALS</a><a href="#">YOUR PLAN</a>
</nav>

<section class="intro">
  <p>Lorem ipsum dolor sit amet, consectetur adipiscing elit, sed do eiusmod tempor incididunt ut labore et dolore magna aliqua. Ut enim ad minim veniam, quis nostrud exercitation ullamco laboris nisi ut aliquip ex ea commodo consequat. Duis aute irure dolor in reprehenderit in voluptate velit esse cillum dolore eu fugiat nulla pariatur. Excepteur sint occaecat cupidatat non proident, sunt in culpa qui officia deserunt mollit anim id est laborum. Duis aute irure dolor in reprehenderit in voluptate velit esse cillum dolore eu fugiat nulla pariatur. Excepteur sint occaecat cupidatat non proident, sunt in culpa qui officia deserunt mollit anim id est laborum.</p>
  <p>Lorem ipsum dolor sit amet, consectetur adipiscing elit, sed do eiusmod tempor incididunt ut labore et dolore magna aliqua. Ut enim ad minim veniam, quis nostrud exercitation ullamco laboris nisi ut aliquip ex ea commodo consequat. Lorem ipsum dolor sit amet, consectetur adipiscing elit, sed do eiusmod tempor incididunt ut labore et dolore magna aliqua. Ut enim ad minim veniam, quis nostrud exercitation ullamco laboris nisi ut aliquip ex ea commodo consequat.</p>
</section>

<main class="panels">
  <section class="panel who">
    <h2 class="panel-head">WHO YOU ARE</h2>
    <div class="panel-body">
      <div class="field"><label>Logo</label><div class="row"><div class="input"></div><button class="btn upload">Upload</button></div></div>
      <div class="field"><label>Business Name</label><div class="row"><div class="input"></div></div></div>
      <div class="field"><label>Business Tag Line</label><div class="row"><div class="input"></div></div></div>
      <div class="field"><label>Business Vision</label><div class="row"><div class="input"></div></div></div>
      <div class="field"><label>Business Bio</label><div class="row"><div class="input"></div></div></div>
      <div class="field"><label>Brand Colours</label>
        <div class="row">
          <div class="swatch-btn"><svg width="17" height="17" viewBox="0 0 17 17"><rect x="0" y="0" width="5" height="5" fill="#f2a36b"/><rect x="6" y="0" width="5" height="5" fill="#e86c8a"/><rect x="12" y="0" width="5" height="5" fill="#cc8eb2"/><rect x="0" y="6" width="5" height="5" fill="#a6d96a"/><rect x="6" y="6" width="5" height="5" fill="#f6d84a"/><rect x="12" y="6" width="5" height="5" fill="#b08cd9"/><rect x="0" y="12" width="5" height="5" fill="#76d6c8"/><rect x="6" y="12" width="5" height="5" fill="#68c7ff"/><rect x="12" y="12" width="5" height="5" fill="#7b8ef0"/></svg></div>
          <div class="input">#333555</div>
        </div>
      </div>
      <div class="actions"><button class="btn submit">SUBMIT</button></div>
    </div>
    <div class="picker">
      <span><i style="background:#ff5252"></i></span><span><i style="background:#5a73ff"></i></span><span><i style="background:#2ef2f2"></i></span><span><i style="background:#6ee8b0"></i></span><span><i style="background:#ffff14"></i></span><span><i style="background:#ffa840"></i></span>
      <span><i style="background:#ff1744"></i></span><span><i style="background:#3d5afe"></i></span><span><i style="background:#00e5ff"></i></span><span><i style="background:#00e676"></i></span><span><i style="background:#ffea00"></i></span><span><i style="background:#ff9100"></i></span>
      <span><i style="background:#d50000"></i></span><span><i style="background:#304ffe"></i></span><span><i style="background:#00b8d4"></i></span><span><i style="background:#00c853"></i></span><span><i style="background:#ffd600"></i></span><span><i style="background:#ff6d00"></i></span>
    </div>
  </section>

  <section class="panel why">
    <h2 class="panel-head">WHY YOU EXIST</h2>
    <div class="panel-body">
      <div class="field"><label>Who are your ideal customers?</label><div class="row"><div class="input"></div><svg class="info" viewBox="0 0 18 18"><circle cx="9" cy="9" r="9" fill="#76d6c8"/><circle cx="9.6" cy="5" r="1.3" fill="#fff"/><path d="M8 8h2.4l-1.2 6H7.4z" fill="#fff"/></svg></div></div>
      <div class="field"><label>What problem are you trying to solve for them?</label><div class="row"><div class="input"></div><svg class="info" viewBox="0 0 18 18"><circle cx="9" cy="9" r="9" fill="#76d6c8"/><circle cx="9.6" cy="5" r="1.3" fill="#fff"/><path d="M8 8h2.4l-1.2 6H7.4z" fill="#fff"/></svg></div></div>
      <div class="field"><label>What pain points will this remove for them?</label><div class="row"><div class="input"></div><svg class="info" viewBox="0 0 18 18"><circle cx="9" cy="9" r="9" fill="#76d6c8"/><circle cx="9.6" cy="5" r="1.3" fill="#fff"/><path d="M8 8h2.4l-1.2 6H7.4z" fill="#fff"/></svg></div></div>
      <div class="field"><label>How do you solve it?</label><div class="row"><div class="input"></div><svg class="info" viewBox="0 0 18 18"><circle cx="9" cy="9" r="9" fill="#76d6c8"/><circle cx="9.6" cy="5" r="1.3" fill="#fff"/><path d="M8 8h2.4l-1.2 6H7.4z" fill="#fff"/></svg></div></div>
      <div class="field"><label>How else could this problem be solved?</label><div class="row"><div class="input"></div><svg class="info" viewBox="0 0 18 18"><circle cx="9" cy="9" r="9" fill="#76d6c8"/><circle cx="9.6" cy="5" r="1.3" fill="#fff"/><path d="M8 8h2.4l-1.2 6H7.4z" fill="#fff"/></svg></div></div>
      <div class="field"><label>Who offers these other solutions?</label><div class="row"><div class="input"></div><svg class="info" viewBox="0 0 18 18"><circle cx="9" cy="9" r="9" fill="#76d6c8"/><circle cx="9.6" cy="5" r="1.3" fill="#fff"/><path d="M8 8h2.4l-1.2 6H7.4z" fill="#fff"/></svg></div></div>
      <div class="field"><label>Why is your solution better?</label><div class="row"><div class="input"></div><svg class="info" viewBox="0 0 18 18"><circle cx="9" cy="9" r="9" fill="#76d6c8"/><circle cx="9.6" cy="5" r="1.3" fill="#fff"/><path d="M8 8h2.4l-1.2 6H7.4z" fill="#fff"/></svg></div></div>
      <div class="field"><label>How much does your solution cost?</label><div class="row"><div class="input"></div><svg class="info" viewBox="0 0 18 18"><circle cx="9" cy="9" r="9" fill="#76d6c8"/><circle cx="9.6" cy="5" r="1.3" fill="#fff"/><path d="M8 8h2.4l-1.2 6H7.4z" fill="#fff"/></svg></div></div>
      <div class="field"><label>What value are you providing to justify this cost?</label><div class="row"><div class="input"></div><svg class="info" viewBox="0 0 18 18"><circle cx="9" cy="9" r="9" fill="#76d6c8"/><circle cx="9.6" cy="5" r="1.3" fill="#fff"/><path d="M8 8h2.4l-1.2 6H7.4z" fill="#fff"/></svg></div></div>
      <div class="field"><label>How will this make their life/job easier/better?</label><div class="row"><div class="input"></div><svg class="info" viewBox="0 0 18 18"><circle cx="9" cy="9" r="9" fill="#76d6c8"/><circle cx="9.6" cy="5" r="1.3" fill="#fff"/><path d="M8 8h2.4l-1.2 6H7.4z" fill="#fff"/></svg></div></div>
      <div class="actions"><button class="btn submit">SUBMIT</button></div>
    </div>
  </section>
</main>

<footer class="footer">Copyright © 2017 Budline.</footer>
</body>
</html>
```